Business card por a urban DJ, up scale audience target

Need a sober design, modern, conservative colors but i can consider some options, y play rnb, hip hop, EDM and top40.

Business card for contact and personal info, double sided, use logo attrached please; im 42 so i need a card acording to my age an target audience.

Target Market(s)

Adult people, up scale audience

Industry/Entity Type

Music Download

Contact Information for Business Card

Cel (574) 3209415586 www.lumaverso.com

Requirements
Must have
• open mind
Nice to have
• open mind
Should not have
• DJ

```html
<!DOCTYPE html>
<html lang="en">
<head>
<meta charset="utf-8">
<title>Lumaverso Business Card</title>
<link href="https://fonts.googleapis.com/css2?family=Open+Sans:wght@400;600;800&display=swap" rel="stylesheet">
<style>
  :root {
    --backdrop: #1f1f1f;
    --card-dark: #2e2d2d;
    --card-light: #ffffff;
    --accent-grey: #b3b3b3;
    --ink-light: #ffffff;
    --ink-dark: #2e2d2d;
  }
  * { margin: 0; padding: 0; box-sizing: border-box; }
  html, body {
    width: 1200px;
    height: 1189px;
    overflow: hidden;
    background: var(--backdrop);
    font-family: "Open Sans", Arial, sans-serif;
  }
  .sheet {
    width: 1200px;
    height: 1189px;
    display: flex;
    flex-direction: column;
    align-items: center;
    justify-content: center;
    gap: 70px;
  }
  .card {
    position: relative;
    width: 840px;
    height: 480px;
    overflow: hidden;
    box-shadow: 0 18px 40px rgba(0,0,0,0.45);
  }
  .card-front {
    background: var(--card-dark);
    display: flex;
    align-items: center;
    justify-content: center;
  }
  .brand-name {
    font-weight: 800;
    letter-spacing: 4px;
    text-transform: uppercase;
  }
  .card-front .brand-name {
    color: var(--ink-light);
    font-size: 86px;
  }
  .card-back .backdrop-shape {
    position: absolute;
    inset: 0;
  }
  .card-back .brand-name {
    position: absolute;
    left: 40px;
    width: 380px;
    top: 205px;
    text-align: center;
    color: var(--ink-dark);
    font-size: 50px;
    letter-spacing: 2px;
  }
  .holder {
    position: absolute;
    left: 520px;
    top: 110px;
    color: var(--ink-light);
    line-height: 1.15;
  }
  .holder-name { font-size: 22px; font-weight: 400; }
  .holder-role { font-size: 20px; font-weight: 600; }
  .contact-list {
    position: absolute;
    left: 560px;
    top: 318px;
    list-style: none;
    color: var(--ink-light);
  }
  .contact-item {
    display: flex;
    align-items: center;
    gap: 14px;
    height: 32px;
    font-size: 20px;
  }
  .contact-item.strong { font-weight: 600; font-size: 22px; }
  .contact-icon { width: 20px; height: 20px; flex: none; }
</style>
</head>
<body>
<main class="sheet">
  <section class="card card-front" aria-label="Card front">
    <span class="brand-name">Lumaverso</span>
  </section>

  <section class="card card-back" aria-label="Card back">
    <svg class="backdrop-shape" viewBox="0 0 840 480" width="840" height="480" aria-hidden="true">
      <rect width="840" height="480" fill="var(--card-dark)"/>
      <path d="M0,0 H445 Q540,200 500,480 H0 Z" fill="var(--accent-grey)"/>
      <path d="M0,0 H410 Q505,200 465,480 H0 Z" fill="var(--card-light)"/>
    </svg>

    <span class="brand-name">Lumaverso</span>

    <div class="holder">
      <p class="holder-name">JONATHAN DOE</p>
      <p class="holder-role">Managing Director</p>
    </div>

    <ul class="contact-list">
      <li class="contact-item">
        <svg class="contact-icon" viewBox="0 0 20 20" aria-hidden="true">
          <rect width="20" height="20" fill="#fff"/>
          <path d="M5,4 L8,4 L9,7 L7.5,8.5 Q9,11.5 11.5,12.5 L13,11 L16,12 L16,15 Q9,16 5,4 Z" fill="var(--card-dark)"/>
        </svg>
        <span>(574) 3209415586</span>
      </li>
      <li class="contact-item strong">
        <svg class="contact-icon" viewBox="0 0 20 20" aria-hidden="true">
          <rect width="20" height="20" fill="#fff"/>
          <rect x="3.5" y="5.5" width="13" height="9" fill="none" stroke="var(--card-dark)" stroke-width="1.4"/>
          <path d="M3.5,5.5 L10,11 L16.5,5.5" fill="none" stroke="var(--card-dark)" stroke-width="1.4"/>
        </svg>
        <span>info@youremail.com</span>
      </li>
      <li class="contact-item">
        <svg class="contact-icon" viewBox="0 0 20 20" aria-hidden="true">
          <rect width="20" height="20" fill="#fff"/>
          <circle cx="10" cy="10" r="6" fill="none" stroke="var(--card-dark)" stroke-width="1.4"/>
          <ellipse cx="10" cy="10" rx="2.5" ry="6" fill="none" stroke="var(--card-dark)" stroke-width="1.2"/>
          <path d="M4,10 H16" stroke="var(--card-dark)" stroke-width="1.2"/>
        </svg>
        <span>www.lumaverso.com</span>
      </li>
    </ul>
  </section>
</main>
</body>
</html>
```